Buxley's Chowder Cafe (New Website Design)

I want an upgraded, modern, sleek, tasteful website that is easily updated internally. Our current website can be viewed at www.buxleyschowdercafe.example

Target Market(s)

Dining Customers

Industry/Entity Type

Restaurant / Hospitality

Coding

Coded - Design and coding required

Number of Pages Required

4 page

Requirements
Must have
• Modern, artful, sleek.. while maintaining a little vintage Cape Cod

```html
<!DOCTYPE html>
<html lang="en">
<head>
<meta charset="utf-8">
<title>Buxley's Chowder Cafe – Kids Menu</title>
<link href="https://fonts.googleapis.com/css2?family=Mulish:wght@400;600;700&family=Playfair+Display:wght@700&display=swap" rel="stylesheet">
<style>
:root{
  --canvas:#ffffff;
  --announce:#857548;
  --announce-text:#f3ecd8;
  --nav:#181b17;
  --cream:#f8f6ef;
  --ink:#1b1d1c;
  --tile:#171b1c;
  --accent:#c8323a;
  --footer:#171a1b;
  --footer-text:#e9e6dd;
  --footer-muted:#8f8f88;
  --field:#2a2e2f;
  --button:#59634c;
}
*{margin:0;padding:0;box-sizing:border-box}
html,body{width:1200px;height:1200px;overflow:hidden;background:var(--canvas);font-family:"Mulish",sans-serif}
.page{position:absolute;left:140px;top:0;width:920px;height:1200px;background:var(--cream);overflow:hidden}
.announce{position:absolute;left:0;top:0;width:100%;height:29px;background:var(--announce);color:var(--announce-text);font-size:8px;text-align:center;line-height:29px;text-decoration:underline}
.nav{position:absolute;left:0;top:29px;width:100%;height:56px;background:var(--nav);display:flex;align-items:center;justify-content:center;gap:13px;color:var(--footer-text);font-size:8.5px;letter-spacing:.4px}
.nav .brand{font-size:9px;font-weight:700;display:flex;align-items:center;gap:5px;margin:0 8px}
.brand .dot{width:8px;height:8px;border-radius:50%;background:var(--footer-text)}
.hero{position:absolute;left:0;top:85px;width:100%;height:125px;background:linear-gradient(100deg,#6e7679 0%,#b9bcb5 22%,#8a8f84 45%,#4c5a4e 60%,#a5412f 78%,#5b5f48 92%,#39402f 100%)}
.hero-title{position:absolute;left:0;top:85px;width:100%;height:125px;display:flex;align-items:center;justify-content:center;padding-top:20px;font-family:"Playfair Display",serif;font-size:30px;color:#fff;letter-spacing:6px}
.tabs{position:absolute;top:252px;left:0;width:100%;display:flex;justify-content:center;gap:17px;font-size:17px;font-weight:700;letter-spacing:.8px;color:var(--ink)}
.tabs .active{color:var(--accent);text-decoration:underline;text-underline-offset:3px}
.dish{position:absolute;width:171px}
.dish .photo{height:109px;background:var(--tile)}
.dish .caption{display:flex;justify-content:space-between;gap:10px;margin-top:13px;font-size:8.5px;line-height:10.5px;color:var(--ink)}
.footer{position:absolute;left:0;top:870px;width:100%;height:330px;background:var(--footer);color:var(--footer-text)}
.footer .brand{position:absolute;left:0;top:62px;width:100%;justify-content:center;display:flex;font-size:13px}
.social{position:absolute;top:114px;left:0;width:100%;display:flex;justify-content:center;gap:18px}
.social span{width:8px;height:8px;border-radius:50%;background:var(--footer-text)}
.f-head{position:absolute;font-size:8.5px;color:var(--footer-muted)}
.links{position:absolute;left:90px;top:174px;list-style:none;font-size:8.5px;line-height:21.5px}
.vip-title{position:absolute;left:208px;top:155px;font-size:8.5px}
.field{position:absolute;height:19px;background:var(--field);border-radius:2px;font-size:6px;color:#cfcbc2;padding:7px 8px 0}
.signup{position:absolute;left:311px;top:221px;width:48px;height:22px;background:var(--button);border-radius:3px;font-size:8px;text-align:center;line-height:22px}
.hours{position:absolute;left:497px;top:174px;width:216px;font-size:7px;line-height:13px}
.hours div{display:flex;align-items:baseline}
.hours i{flex:1;border-bottom:1px solid #777;margin:0 2px}
.address{position:absolute;left:748px;top:174px;font-size:8.5px;line-height:11px}
</style>
</head>
<body>
<div class="page">
  <div class="announce">Write a Review, Win $500! Help guests by leaving a review of your favorite dishes. Be entered in a drawing to win $500 on 3/1</div>
  <nav class="nav">
    <span>ORDER ONLINE</span><span>OUR MENUS</span><span>SEAFOOD MARKETPLACE</span>
    <span class="brand"><span class="dot"></span>Buxley's</span>
    <span>GIFT CARDS</span><span>ABOUT US</span><span>SIGN IN</span><span>BECOME A VIP</span>
  </nav>
  <div class="hero" role="img" aria-label="Photo of the cafe's shingled storefront with holiday wreaths and a hanging sign"></div>
  <h1 class="hero-title">MENU</h1>

  <div class="tabs"><span>DAILY SPECIALS</span><span>DINNER MENU</span><span class="active">KIDS MENU</span></div>

  <div class="dish" style="left:81px;top:316px"><div class="photo"></div><div class="caption"><span>Kids Baked Scrod w/ potato &amp; vegetable</span><span>$11</span></div></div>
  <div class="dish" style="left:277px;top:316px"><div class="photo"></div><div class="caption"><span>Kids Fish &amp; Chips</span><span>$11</span></div></div>
  <div class="dish" style="left:473px;top:316px"><div class="photo"></div><div class="caption"><span>Kids Chicken Tenders with Fries</span><span>$9</span></div></div>
  <div class="dish" style="left:668px;top:316px"><div class="photo"></div><div class="caption"><span>Kids Grilled Cheese Sandwich with Fries</span><span>$8</span></div></div>
  <div class="dish" style="left:81px;top:481px"><div class="photo"></div><div class="caption"><span>Kids Fried Chicken Sandwich with Fries</span><span>$9</span></div></div>
  <div class="dish" style="left:277px;top:481px"><div class="photo"></div><div class="caption"><span>Kids Chicken Parmesan with Penne Pasta</span><span>$9</span></div></div>
  <div class="dish" style="left:473px;top:481px"><div class="photo"></div><div class="caption"><span>Kids Hot Dog with Fries</span><span>$10</span></div></div>
  <div class="dish" style="left:668px;top:481px"><div class="photo"></div><div class="caption"><span>Kids Penne Pasta with Marinara Sauce</span><span>$8</span></div></div>
  <div class="dish" style="left:375px;top:645px"><div class="photo"></div><div class="caption"><span>Kids Grilled Chicken w/ potato &amp; vegetable</span><span>$9</span></div></div>

  <footer class="footer">
    <div class="brand"><span>Buxley's</span></div>
    <div class="social"><span></span><span></span></div>

    <div class="f-head" style="left:90px;top:158px">Links</div>
    <ul class="links">
      <li>Order Online</li><li>Our Menu</li><li>Seafood Marketplace</li><li>Gift Cards</li><li>Our Story</li><li>Our Gallery</li>
    </ul>

    <div class="vip-title">BECOME VIP</div>
    <div class="field" style="left:208px;top:168px;width:124px">Email</div>
    <div class="field" style="left:337px;top:168px;width:124px">Full Name</div>
    <div class="field" style="left:208px;top:193px;width:253px">Mobile Phone (optional)</div>
    <div class="signup">Sign Up</div>

    <div class="f-head" style="left:497px;top:158px">Hours</div>
    <div class="hours">
      <div><span>Monday–Tuesday</span><i></i><span>Closed</span></div>
      <div><span>Wednesday–Sunday</span><i></i><span>11:30am–9pm</span></div>
    </div>

    <div class="f-head" style="left:748px;top:158px">Address</div>
    <div class="address">
      <p style="margin-bottom:5px">Harborview</p>
      <p>118 Dune Rd</p>
      <p style="margin-bottom:4px">Harborview, MA 02600</p>
      <p>(508) 555-0142</p>
    </div>
  </footer>
</div>
</body>
</html>
```